Brava Stone Oven Kitchen (restaurant)

Restaurant with a cool vibe.
We need a refresh of existing site. Appealing to a hip crowd of 25 or older age bracket (mid price to high small town). Constant changes food and cocktail menu. A vibing atmosphere with jazz funk hip music.
Must be able to scale for any device… phone/mobile device super important.
Instagram: @Brava.Linwell
Website: bravalinwell.example

Target Market(s)

25-55 age group

Number of Pages Required

1 page

Font styles to use
Sans Serif

Requirements
Must have
• Simple to navigate. Simplicity is the key to all sophistication.

Links/Buttons
Menu
Gift Cards
Reservations
Take Out
Contact Us
Should not have
• Please, nothing generic looking… no cookie cutter look. Originality

```html
<!DOCTYPE html>
<html lang="en">
<head>
<meta charset="utf-8">
<title>Brava Stone Oven Kitchen</title>
<link href="https://fonts.googleapis.com/css2?family=Red+Hat+Display:wght@500;600;700;800&family=Open+Sans:wght@400;600;700&family=Oswald:wght@700&display=swap" rel="stylesheet">
<style>
:root{
  --red:#e5383f;
  --red-deep:#c62c33;
  --ink:#111111;
  --text:#2b2b2b;
  --muted:#444444;
  --paper:#ffffff;
  --frame-grey:#e9e9e9;
  --black:#000000;
  --display:"Red Hat Display", sans-serif;
  --body:"Open Sans", sans-serif;
  --condensed:"Oswald", sans-serif;
}
*{box-sizing:border-box;margin:0;padding:0}
html,body{width:1200px;height:2523px;overflow:hidden}
body{position:relative;font-family:var(--body);color:var(--text);background:var(--paper)}
.abs{position:absolute}
svg{display:block}

/* hero */
.hero{position:absolute;left:0;top:0;width:1200px;height:621px;overflow:hidden}
.hero-photo{position:absolute;inset:0;background:radial-gradient(ellipse at 70% 45%,#5c4032 0%,#3c2a20 40%,#241912 100%)}
.hero-shade{position:absolute;inset:0;background:rgba(0,0,0,.25)}
.topbar{position:absolute;left:0;top:0;width:1200px;height:36px;border-bottom:1px solid rgba(255,255,255,.25);color:#fff;font-size:11px}
.topbar .contact{position:absolute;top:9px;display:flex;align-items:center;gap:8px}
.topbar .socials{position:absolute;right:150px;top:10px;display:flex;gap:18px}
.dot-icon{width:13px;height:13px;border:1.6px solid #fff;border-radius:50%}
.brand{position:absolute;left:150px;top:58px;color:#fff;font-family:var(--display);font-weight:700;line-height:1}
.brand .name{font-size:31px;letter-spacing:1.5px;text-transform:uppercase}
.brand .tag{font-size:10px;margin-top:2px;padding-left:16px}
.nav{position:absolute;left:420px;top:70px;display:flex;gap:17px;font-family:var(--display);font-weight:600;font-size:14px;color:#fff}
.nav-tools{position:absolute;left:1002px;top:71px;display:flex;gap:18px}
.hero-copy{position:absolute;left:0;top:196px;width:1200px;text-align:center;color:#fff}
.hero-copy h1{font-family:var(--display);font-weight:700;font-size:37px;line-height:46px}
.hero-copy p{width:520px;margin:26px auto 0;font-family:var(--display);font-weight:600;font-size:13.5px;line-height:23px}
.btn-outline{display:inline-block;margin-top:24px;width:105px;height:33px;border:1px solid #fff;line-height:31px;font-family:var(--display);font-weight:600;font-size:13px;color:#fff}

/* menu */
.menu-section{position:absolute;left:0;top:621px;width:1200px;height:825px;background:var(--red)}
.section-title{font-family:var(--display);font-weight:700;text-align:center;color:#fff}
.menu-section .section-title{position:absolute;top:46px;width:1200px;font-size:35px}
.menu-frame{position:absolute;left:150px;top:125px;width:900px;height:600px;background:var(--red-deep);padding:12px}
.menu-frame-inner{width:100%;height:100%;background:var(--paper);padding:11px}
.menu-board{width:100%;height:100%;background:var(--frame-grey);padding:12px;display:flex;gap:18px}
.menu-card{width:407px;height:531px;background:var(--paper);padding:22px 21px 0 24px}
.menu-card h2{font-family:var(--display);font-weight:700;font-size:37px;line-height:40px;color:var(--ink);height:44px;border-bottom:2px solid var(--red)}
.menu-list{list-style:none;margin-top:22px}
.menu-item{display:flex;gap:10px;height:97.5px}
.dish-photo{width:68px;height:68px;border-radius:50%;flex:none}
.dish-a{background:radial-gradient(circle,#4f6a2e 0%,#2a2d22 60%,#4a3a2a 100%)}
.dish-b{background:radial-gradient(circle,#b8652a 0%,#7a4a2c 60%,#c9c2b6 100%)}
.dish-c{background:radial-gradient(circle,#c2452f 0%,#d69a4a 55%,#e8ddc8 100%)}
.dish-d{background:radial-gradient(circle,#d9a27a 0%,#6f8a3a 55%,#efe6d8 100%)}
.dish-info{flex:1;padding-top:2px}
.dish-head{display:flex;justify-content:space-between;font-size:14.5px;color:var(--ink);padding-bottom:10px;border-bottom:1px dashed #777}
.dish-head .price{color:var(--red)}
.dish-info p{font-size:11.5px;line-height:18.5px;color:var(--muted);margin-top:6px}

/* reservation */
.reservation{position:absolute;left:0;top:1446px;width:1200px;height:326px;overflow:hidden}
.reservation-photo{position:absolute;inset:0;background:linear-gradient(180deg,#2a1d16 0%,#3a2518 45%,#4a2a22 75%,#26170f 100%)}
.reservation-shade{position:absolute;inset:0;background:rgba(0,0,0,.35)}
.reservation .section-title{position:absolute;top:35px;width:1200px;font-size:37px}
.hours{position:absolute;top:103px;width:1200px;text-align:center;color:#fff;font-family:var(--display);font-weight:700;font-size:13.5px}
.field{position:absolute;height:37px;border:1px solid #fff;color:#fff;font-size:11.5px;line-height:35px;padding-left:19px}
.field svg{position:absolute;right:10px;top:11px}
.btn-book{position:absolute;left:840px;top:204px;width:210px;height:37px;background:var(--red);color:#fff;font-family:var(--display);font-weight:700;font-size:14px;text-align:center;line-height:37px}

/* voucher */
.voucher{position:absolute;left:150px;top:1810px;width:900px;height:375px;background:var(--red);border-radius:12px}
.voucher-art{position:absolute;left:21px;top:83px;width:221px;height:207px;background:linear-gradient(160deg,#f4f4f4 0%,#dcdcdc 100%)}
.voucher h2{position:absolute;left:307px;top:95px;font-family:var(--condensed);font-weight:700;font-size:38px;letter-spacing:.5px;color:#fff}
.voucher p{position:absolute;left:307px;top:165px;width:495px;color:#fff;font-size:14.5px;line-height:18px}
.btn-pill{position:absolute;left:308px;top:252px;width:135px;height:36px;border-radius:18px;background:#fff;color:var(--ink);font-family:var(--display);font-weight:700;font-size:13px;text-align:center;line-height:36px}

/* footer */
.footer{position:absolute;left:0;top:2223px;width:1200px;height:266px;background:var(--black);color:#fff}
.footer .brand{top:50px}
.footer-about{position:absolute;left:150px;top:108px;width:210px;font-size:11.5px;line-height:18px}
.footer h3{position:absolute;font-family:var(--body);font-weight:700;font-size:14px}
.newsletter{position:absolute;left:476px;top:82px;display:flex}
.newsletter .email{width:158px;height:33px;background:#fff;color:#777;font-size:11px;line-height:33px;padding-left:8px}
.newsletter .subscribe{width:89px;height:33px;background:var(--red);font-family:var(--body);font-weight:700;font-size:12px;text-align:center;line-height:33px}
.footer-social{position:absolute;left:474px;top:141px;display:flex;gap:24px}
.footer-social .dot-icon{width:16px;height:16px}
.touch{position:absolute;left:875px;top:81px;list-style:none;font-size:11px;line-height:18px}
.touch li{display:flex;align-items:center;gap:9px}
.copyright{position:absolute;left:0;top:2489px;width:1200px;height:34px;background:var(--red);color:#fff;text-align:center;font-size:14.5px;line-height:34px}
</style>
</head>
<body>

<header class="hero">
  <div class="hero-photo" role="img" aria-label="Close-up photo of grilled chicken wraps with fresh greens and peppers on a rustic wooden table"></div>
  <div class="hero-shade"></div>

  <div class="topbar">
    <div class="contact" style="left:150px">
      <svg width="13" height="13" viewBox="0 0 24 24"><path fill="#fff" d="M6.6 10.8a15 15 0 0 0 6.6 6.6l2.2-2.2c.3-.3.7-.4 1-.2 1.1.4 2.3.6 3.6.6.6 0 1 .4 1 1V20c0 .6-.4 1-1 1A17 17 0 0 1 3 4c0-.6.4-1 1-1h3.5c.6 0 1 .4 1 1 0 1.3.2 2.5.6 3.6.1.3 0 .7-.2 1z"/></svg>
      <span>555-013-0142</span>
    </div>
    <div class="contact" style="left:266px">
      <svg width="15" height="11" viewBox="0 0 16 12"><rect x=".5" y=".5" width="15" height="11" fill="none" stroke="#fff"/><path d="M.5.5 8 7l7.5-6.5" fill="none" stroke="#fff"/></svg>
      <span>hello@bravalinwell.example</span>
    </div>
    <div class="socials" aria-label="Social links">
      <span class="dot-icon"></span><span class="dot-icon"></span><span class="dot-icon"></span>
    </div>
  </div>

  <div class="brand"><div class="name">Brava</div><div class="tag">Stone Oven Kitchen</div></div>

  <nav class="nav"><span>CONTACT</span><span>MENU</span><span>RESERVATIONS</span><span>ORDER ONLINE</span></nav>
  <div class="nav-tools">
    <svg width="14" height="14" viewBox="0 0 16 16"><circle cx="6.5" cy="6.5" r="5" fill="none" stroke="#e5383f" stroke-width="1.6"/><path d="M10.2 10.2 15 15" stroke="#e5383f" stroke-width="1.6"/></svg>
    <svg width="15" height="14" viewBox="0 0 16 15"><path d="M1 1h2.5l2 9h8l1.5-6H4.5" fill="none" stroke="#fff" stroke-width="1.3"/><circle cx="6.5" cy="13" r="1.1" fill="#fff"/><circle cx="12" cy="13" r="1.1" fill="#fff"/></svg>
  </div>

  <div class="hero-copy">
    <h1>Lets Get Lunch At<br>Brava!</h1>
    <p>Lorem ipsum dolor sit amet, consectetur adipiscing elit, sed do eiusmod tempor incididunt ut labore et dolore magna aliqua. Quis ipsum suspendisse ultrices gravida. Risus commodo viverra maecenas accumsan lacus vel facilisis.</p>
    <span class="btn-outline">ORDER NOW</span>
  </div>
</header>

<section class="menu-section">
  <h2 class="section-title">OUR MENU</h2>
  <div class="menu-frame"><div class="menu-frame-inner"><div class="menu-board">

    <article class="menu-card">
      <h2>DINING</h2>
      <ul class="menu-list">
        <li class="menu-item"><div class="dish-photo dish-a" role="img" aria-label="Bowl of wood fired brussels sprouts"></div><div class="dish-info"><div class="dish-head"><span>Wood Fired Brussels Sprouts</span><span class="price">$25</span></div><p>Smoked bacon, parmesan,fresh lemon,<br>cherry tomato,garlic aioli / 13</p></div></li>
        <li class="menu-item"><div class="dish-photo dish-b" role="img" aria-label="Butternut and sausage skewers"></div><div class="dish-info"><div class="dish-head"><span>Butternut &amp; Sausage Skewers</span><span class="price">$20</span></div><p>Roasted butternut squash, grilled sausage,<br>herbed ricotta, fresh arugula &amp; cherry tomato</p></div></li>
        <li class="menu-item"><div class="dish-photo dish-c" role="img" aria-label="Pita with two dips"></div><div class="dish-info"><div class="dish-head"><span>Pita Dip Duo</span><span class="price">$55</span></div><p>House-made spicy red pepper feta dip,<br>roasted garlic &amp; spinach hummus, grilled pita</p></div></li>
        <li class="menu-item"><div class="dish-photo dish-d" role="img" aria-label="Flatbread with arugula"></div><div class="dish-info"><div class="dish-head"><span>Magnolia Flatbread</span><span class="price">$26</span></div><p>Balsamic onion jam, smoked bacon, goat<br>cheese, fresh arugula &amp; balsamic drizzle / 15</p></div></li>
      </ul>
    </article>

    <article class="menu-card">
      <h2>TAKEOUT</h2>
      <ul class="menu-list">
        <li class="menu-item"><div class="dish-photo dish-a" role="img" aria-label="Bowl of wood fired brussels sprouts"></div><div class="dish-info"><div class="dish-head"><span>Wood Fired Brussels Sprouts</span><span class="price">$25</span></div><p>Smoked bacon, parmesan,fresh lemon,<br>cherry tomato,garlic aioli / 13</p></div></li>
        <li class="menu-item"><div class="dish-photo dish-b" role="img" aria-label="Butternut and sausage skewers"></div><div class="dish-info"><div class="dish-head"><span>Butternut &amp; Sausage Skewers</span><span class="price">$20</span></div><p>Roasted butternut squash, grilled sausage,<br>herbed ricotta, fresh arugula &amp; cherry tomato</p></div></li>
        <li class="menu-item"><div class="dish-photo dish-c" role="img" aria-label="Pita with two dips"></div><div class="dish-info"><div class="dish-head"><span>Pita Dip Duo</span><span class="price">$55</span></div><p>House-made spicy red pepper feta dip,<br>roasted garlic &amp; spinach hummus, grilled pita</p></div></li>
        <li class="menu-item"><div class="dish-photo dish-d" role="img" aria-label="Flatbread with arugula"></div><div class="dish-info"><div class="dish-head"><span>Magnolia Flatbread</span><span class="price">$26</span></div><p>Balsamic onion jam, smoked bacon, goat<br>cheese, fresh arugula &amp; balsamic drizzle / 15</p></div></li>
      </ul>
    </article>

  </div></div></div>
</section>

<section class="reservation">
  <div class="reservation-photo" role="img" aria-label="Dim restaurant dining room with checkered tablecloths and wine shelves"></div>
  <div class="reservation-shade"></div>
  <h2 class="section-title">RESERVATION</h2>
  <div class="hours">OPENING HOUR THURSDAY TO SUNDAY 12:00PM – 9:00PM</div>
  <div class="field" style="left:150px;top:138px;width:210px">Name</div>
  <div class="field" style="left:380px;top:138px;width:209px">Email</div>
  <div class="field" style="left:610px;top:138px;width:209px">Phone</div>
  <div class="field" style="left:840px;top:138px;width:210px">mm/dd/yyyy
    <svg width="13" height="13" viewBox="0 0 14 14"><rect x="1" y="2" width="12" height="11" fill="none" stroke="#e5383f" stroke-width="1.2"/><path d="M1 5h12M4 1v2M10 1v2" stroke="#e5383f" stroke-width="1.2"/></svg></div>
  <div class="field" style="left:150px;top:204px;width:210px">Time
    <svg width="13" height="13" viewBox="0 0 14 14"><circle cx="7" cy="7" r="6" fill="none" stroke="#e5383f" stroke-width="1.2"/><path d="M7 3.5V7l2.5 1.5" fill="none" stroke="#e5383f" stroke-width="1.2"/></svg></div>
  <div class="field" style="left:380px;top:204px;width:439px">Message</div>
  <div class="btn-book">BOOK A TABLE</div>
</section>

<section class="voucher">
  <div class="voucher-art" role="img" aria-label="Open envelope holding a spa gift voucher card"></div>
  <h2>SPA VOUCHER FOR $50</h2>
  <p>Lorem ipsum dolor sit amet, consectetur adipiscing elit, sed do eiusmod tempor incididunt ut labore et dolore magna aliqua. Quis ipsum suspendisse ultrices gravida. Risus commodo viverra maecenas accumsan lacus vel facilisis.</p>
  <span class="btn-pill">BOOK NOW</span>
</section>

<footer class="footer">
  <div class="brand"><div class="name">Brava</div><div class="tag">Stone Oven Kitchen</div></div>
  <p class="footer-about">Lorem ipsum dolor sit amet, consectetur adipiscing elit, sed do eiusmod tempor incididunt ut labore et dolore magna</p>

  <h3 style="left:475px;top:47px">Newsletter</h3>
  <div class="newsletter"><span class="email">Enter Your Email</span><span class="subscribe">SUBSCRIBE</span></div>
  <div class="footer-social" aria-label="Social links">
    <span class="dot-icon"></span><span class="dot-icon"></span><span class="dot-icon"></span><span class="dot-icon"></span><span class="dot-icon"></span>
  </div>

  <h3 style="left:875px;top:47px">Get In Touch</h3>
  <ul class="touch">
    <li><svg width="9" height="11" viewBox="0 0 10 13"><path fill="#fff" d="M5 0a5 5 0 0 0-5 5c0 3.5 5 8 5 8s5-4.5 5-8a5 5 0 0 0-5-5zm0 7a2 2 0 1 1 0-4 2 2 0 0 1 0 4z"/></svg>48 Harlow Street Linwell, ON</li>
    <li><svg width="9" height="9" viewBox="0 0 24 24"><path fill="#fff" d="M6.6 10.8a15 15 0 0 0 6.6 6.6l2.2-2.2c.3-.3.7-.4 1-.2 1.1.4 2.3.6 3.6.6.6 0 1 .4 1 1V20c0 .6-.4 1-1 1A17 17 0 0 1 3 4c0-.6.4-1 1-1h3.5c.6 0 1 .4 1 1 0 1.3.2 2.5.6 3.6.1.3 0 .7-.2 1z"/></svg>555-013-0142</li>
    <li><svg width="10" height="8" viewBox="0 0 16 12"><rect x=".5" y=".5" width="15" height="11" fill="none" stroke="#fff" stroke-width="1.5"/><path d="M.5.5 8 7l7.5-6.5" fill="none" stroke="#fff" stroke-width="1.5"/></svg>hello@bravalinwell.example</li>
  </ul>
</footer>

<div class="copyright">Copyright © 2021 Brava</div>

</body>
</html>
```